Book Flyer

I want a flyer that we can use to promote this book to educators and to leaders....below is a sample flyer but I want something bold and creative and different from this....it can be completely different from what is attached. I want to be a WOW to increase sales. Please include pic of book and how folks can get a copy....I've given you a few pics but please be creative ....looking for a wow.

```html
<!DOCTYPE html>
<html lang="en">
<head>
<meta charset="UTF-8">
<title>Intentional Excellence – Book Flyer</title>
<link rel="stylesheet" href="https://fonts.googleapis.com/css2?family=Anton&family=Yellowtail&family=Libre+Baskerville:wght@400;700&family=Mulish:wght@400;600&family=Montserrat:wght@700;800&family=Oswald:wght@500;600&display=swap">
<style>
  :root {
    --navy: #1f3a52;
    --navy-deep: #0f1b27;
    --steel: #2d4a63;
    --city-top: #5f7688;
    --city-low: #1d3347;
    --red: #a00b12;
    --red-bright: #c8141c;
    --neon: #f3f0a0;
    --white: #ffffff;
    --ink: #111111;
    --paper: #f7f7f7;
  }
  * { box-sizing: border-box; margin: 0; padding: 0; }
  html, body { width: 947px; height: 1200px; overflow: hidden; background: var(--white); }
  .flyer { position: relative; width: 947px; height: 1200px; overflow: hidden; background: var(--paper); }

  .city-scene {
    position: absolute; left: 0; top: 0; width: 947px; height: 326px;
    background: linear-gradient(180deg, var(--city-top) 0%, #3e586d 45%, var(--city-low) 100%);
  }
  .intro-panel {
    position: absolute; left: 0; top: 326px; width: 947px; height: 331px;
    background:
      repeating-linear-gradient(135deg, rgba(255,255,255,0.04) 0 2px, transparent 2px 6px),
      linear-gradient(180deg, #2a4a66 0%, #213b52 100%);
  }
  .author-portrait {
    position: absolute; left: 37px; top: 120px; width: 362px; height: 537px;
    border-radius: 150px 150px 0 0;
    background: linear-gradient(180deg, #d9dfe8 0%, #c9d3e3 55%, #5c5f66 80%, #45484e 100%);
  }

  .title-pill {
    position: absolute; left: 385px; top: 86px; width: 562px; height: 122px;
    border-radius: 61px 0 0 61px;
    background: linear-gradient(180deg, var(--red-bright) 0%, #8c0a10 60%, #5e0509 100%);
  }
  .title-main {
    position: absolute; left: 440px; top: 92px; width: 480px;
    font-family: "Anton", "Oswald", sans-serif; font-size: 84px; line-height: 110px;
    color: var(--white); letter-spacing: 0.5px; text-align: center;
  }
  .title-script {
    position: absolute; left: 520px; top: 196px; width: 340px; text-align: center;
    font-family: "Yellowtail", cursive; font-size: 64px; line-height: 80px;
    color: var(--neon); transform: rotate(-6deg);
    text-shadow: 0 0 6px rgba(243,240,160,0.9), 0 0 14px rgba(230,220,90,0.6);
  }

  .book-cover {
    position: absolute; left: 730px; top: 321px; width: 168px; height: 207px;
    background: var(--white); box-shadow: 0 4px 10px rgba(0,0,0,0.45);
    display: flex; flex-direction: column; overflow: hidden;
  }
  .book-cover__art { height: 85px; background: linear-gradient(180deg, #1c2f52 0%, #2a4270 100%); }
  .book-cover__band {
    background: #e0393c; color: var(--white); text-align: center; padding: 4px 0 3px;
  }
  .book-cover__title { font-family: "Oswald", sans-serif; font-weight: 600; font-size: 22px; line-height: 24px; }
  .book-cover__sub { font-family: "Oswald", sans-serif; font-weight: 500; font-size: 10px; color: #fde27a; letter-spacing: 0.5px; }
  .book-cover__tag { font-family: "Mulish", sans-serif; font-size: 4.5px; text-align: center; color: #333; padding: 6px 4px 0; font-weight: 600; }
  .book-cover__author { font-family: "Oswald", sans-serif; font-size: 12px; color: #1d3a70; text-align: right; padding: 14px 10px 0 0; }
  .book-cover__foreword { font-family: "Mulish", sans-serif; font-size: 4.5px; color: #555; text-align: right; padding-right: 10px; letter-spacing: 0.4px; }

  .book-blurb {
    position: absolute; left: 417px; top: 392px; width: 289px;
    font-family: "Libre Baskerville", serif; font-weight: 700; font-size: 12.4px; line-height: 14.3px;
    color: var(--white); text-align: justify;
  }
  .book-blurb__lead { font-size: 14.5px; letter-spacing: 0.6px; display: block; text-align-last: justify; }
  .book-promise {
    position: absolute; left: 417px; top: 540px; width: 418px;
    font-family: "Libre Baskerville", serif; font-weight: 700; font-size: 12.4px; line-height: 14.3px;
    color: var(--white); text-align: justify;
  }
  .testimonial-name {
    position: absolute; right: 128px; top: 598px;
    font-family: "Libre Baskerville", serif; font-weight: 700; font-size: 12.5px; color: var(--white);
  }
  .quote-mark { position: absolute; }
  .quote-mark--large { left: 846px; top: 590px; width: 74px; height: 50px; }

  .about-tab {
    position: absolute; left: 0; top: 603px; width: 400px; height: 54px;
    border-radius: 0 27px 27px 0; background: rgba(45,82,112,0.75);
  }
  .about-tab__label {
    position: absolute; left: 128px; top: 612px;
    font-family: "Libre Baskerville", serif; font-weight: 700; font-size: 22px; color: var(--white);
  }

  .lower-section {
    position: absolute; left: 0; top: 657px; width: 947px; height: 498px;
    background: repeating-linear-gradient(135deg, rgba(0,0,0,0.035) 0 1px, transparent 1px 6px), var(--paper);
  }
  .bio-pill {
    position: absolute; left: 199px; top: 657px; width: 748px; height: 134px;
    border-radius: 0 0 0 67px;
    background: repeating-linear-gradient(135deg, rgba(255,255,255,0.03) 0 2px, transparent 2px 6px), var(--navy-deep);
  }
  .bio-pill::before {
    content: ""; position: absolute; left: 0; top: 0; width: 67px; height: 67px;
    border-radius: 67px 0 0 0; background: var(--navy-deep);
  }
  .bio-text {
    position: absolute; left: 262px; top: 671px; width: 654px;
    font-family: "Libre Baskerville", serif; font-size: 14px; line-height: 17px;
    color: var(--white); text-align: justify;
  }

  .strategies-heading {
    position: absolute; left: 0; top: 820px; width: 947px; height: 40px;
  }
  .strategies-heading__rule { position: absolute; top: 20px; height: 3px; background: var(--navy); }
  .strategies-heading__rule--left { left: 0; width: 95px; }
  .strategies-heading__rule--right { left: 842px; width: 105px; }
  .strategies-heading__text {
    position: absolute; left: 188px; top: 0; white-space: nowrap;
    font-family: "Mulish", sans-serif; font-size: 25px; line-height: 40px; color: var(--navy); letter-spacing: 0.3px;
  }
  .strategies-heading__num { color: var(--red); font-size: 40px; margin-right: 14px; vertical-align: -4px; }

  .strategy { position: absolute; top: 872px; width: 220px; text-align: center; }
  .strategy--equity { left: 153px; }
  .strategy--change { left: 368px; }
  .strategy--communication { left: 584px; }
  .strategy__icon {
    width: 92px; height: 92px; margin: 0 auto; border-radius: 50%; background: var(--red);
    display: flex; align-items: center; justify-content: center;
  }
  .strategy__title {
    margin-top: 18px; font-family: "Montserrat", sans-serif; font-weight: 800; font-size: 18.5px; color: var(--ink);
  }
  .strategy__quote {
    margin-top: 6px; font-family: "Libre Baskerville", serif; font-size: 12.2px; line-height: 15.5px; color: #222;
  }
  .strategy__source {
    position: absolute; left: 0; width: 220px; top: 214px;
    font-family: "Libre Baskerville", serif; font-weight: 700; font-size: 11px; color: var(--ink);
  }
  .strategy__mark { position: absolute; top: 232px; width: 22px; height: 16px; }

  .contact-bar {
    position: absolute; left: 0; top: 1155px; width: 947px; height: 45px;
    background: linear-gradient(90deg, #19324a 0%, #3c6485 50%, #19324a 100%);
    display: flex; align-items: center; justify-content: center; gap: 26px;
  }
  .contact-bar__email { font-family: "Mulish", sans-serif; font-size: 19px; color: var(--white); letter-spacing: 0.6px; }
</style>
</head>
<body>
<main class="flyer">

  <div class="city-scene" role="img" aria-label="Night skyline of a big city with a tall spire tower"></div>
  <div class="intro-panel"></div>
  <div class="author-portrait" role="img" aria-label="Portrait of the author in a white shirt and patterned tie, arms crossed"></div>

  <div class="title-pill"></div>
  <h1 class="title-main">INTENTIONAL</h1>
  <div class="title-script">Excellence</div>

  <div class="book-cover" aria-label="Book cover">
    <div class="book-cover__art" role="img" aria-label="Rising arrows in red, blue and white"></div>
    <div class="book-cover__band">
      <div class="book-cover__title">INTENTIONAL</div>
      <div class="book-cover__sub">EXCELLENCE</div>
    </div>
    <div class="book-cover__tag">3 FUNDAMENTAL STRATEGIES THAT DRIVE EDUCATIONAL LEADERSHIP</div>
    <div class="book-cover__author">R. Marcus Marlowe</div>
    <div class="book-cover__foreword">FOREWORD BY LEON HARTLEY</div>
  </div>

  <p class="book-blurb"><span class="book-blurb__lead">INTENTIONAL EXCELLENCE</span>is a book written for all leaders. Dr.Marlowe speaks from real life experiences that are releable and from the heart. his leadership steps have helped him develop into one of the most accomplished administrative leaders in the country.</p>
  <p class="book-promise">the three specific strategies outlined in this book will transform your leadership skills and help you stay on track to ensure success.</p>
  <p class="testimonial-name">Helen Ashford, Principal</p>
  <svg class="quote-mark quote-mark--large" viewBox="0 0 74 50" aria-hidden="true">
    <g fill="#fff">
      <circle cx="16" cy="34" r="14"/><path d="M4 30 C4 14 14 4 24 2 L26 6 C18 9 14 16 14 24 Z"/>
      <circle cx="56" cy="34" r="14"/><path d="M44 30 C44 14 54 4 64 2 L66 6 C58 9 54 16 54 24 Z"/>
    </g>
  </svg>

  <div class="about-tab"></div>
  <h2 class="about-tab__label">About Dr.Marlowe</h2>

  <section class="lower-section"></section>
  <div class="bio-pill"></div>
  <p class="bio-text">Distinguished as vibrant, visionary and innovative leader who recognizes that humanity is the most important trait a leader can process. Dr.Marlowe uses his prior experiences in business, education and nonprofit to assist organization leaders from all the industries build internal leadership capacity, including strategy &amp; talent management and developement to maximize organizational potential and success.</p>

  <div class="strategies-heading">
    <span class="strategies-heading__rule strategies-heading__rule--left"></span>
    <h2 class="strategies-heading__text"><span class="strategies-heading__num">3</span>Fundamental Strategies That Drive Leadership</h2>
    <span class="strategies-heading__rule strategies-heading__rule--right"></span>
  </div>

  <article class="strategy strategy--equity">
    <div class="strategy__icon">
      <svg width="52" height="46" viewBox="0 0 52 46" aria-hidden="true" fill="none" stroke="#fff" stroke-width="3" stroke-linecap="round" stroke-linejoin="round">
        <circle cx="26" cy="6" r="3" fill="#fff"/>
        <path d="M6 10 L46 10 M26 9 L26 40 M16 40 L36 40"/>
        <path d="M10 10 L3 26 M10 10 L17 26 M2 26 Q10 34 18 26 Z" fill="#fff"/>
        <path d="M42 10 L35 26 M42 10 L49 26 M34 26 Q42 34 50 26 Z" fill="#fff"/>
      </svg>
    </div>
    <h3 class="strategy__title">Equity</h3>
    <p class="strategy__quote">fairness does not mean everyone gets the same Fairness means everyone gets what they need</p>
    <p class="strategy__source">Nora Whitfield</p>
    <svg class="strategy__mark" style="left:168px" viewBox="0 0 22 16" aria-hidden="true"><g fill="#333"><circle cx="5" cy="11" r="4.5"/><path d="M1 10 C1 4 4 1 8 0 L8.6 1.6 C6 3 5 5 5 8 Z"/><circle cx="16" cy="11" r="4.5"/><path d="M12 10 C12 4 15 1 19 0 L19.6 1.6 C17 3 16 5 16 8 Z"/></g></svg>
  </article>

  <article class="strategy strategy--change">
    <div class="strategy__icon">
      <svg width="52" height="52" viewBox="0 0 52 52" aria-hidden="true" fill="none" stroke="#fff" stroke-width="6">
        <path d="M10 24 A16 16 0 0 1 40 16"/>
        <path d="M42 28 A16 16 0 0 1 12 36"/>
        <path d="M34 8 L46 10 L42 22 Z" fill="#fff" stroke="none"/>
        <path d="M18 44 L6 42 L10 30 Z" fill="#fff" stroke="none"/>
      </svg>
    </div>
    <h3 class="strategy__title">Change</h3>
    <p class="strategy__quote">If you don’t change direction, you may end up where are heading</p>
    <p class="strategy__source">Chen Wei-Lin</p>
    <svg class="strategy__mark" style="left:182px" viewBox="0 0 22 16" aria-hidden="true"><g fill="#333"><circle cx="5" cy="11" r="4.5"/><path d="M1 10 C1 4 4 1 8 0 L8.6 1.6 C6 3 5 5 5 8 Z"/><circle cx="16" cy="11" r="4.5"/><path d="M12 10 C12 4 15 1 19 0 L19.6 1.6 C17 3 16 5 16 8 Z"/></g></svg>
  </article>

  <article class="strategy strategy--communication">
    <div class="strategy__icon">
      <svg width="56" height="50" viewBox="0 0 56 50" aria-hidden="true">
        <path d="M22 3 C33 3 42 10 42 19 C42 28 33 35 22 35 L10 42 L13 32 C6 29 2 24 2 19 C2 10 11 3 22 3 Z" fill="#fff"/>
        <path d="M36 18 C46 18 54 24 54 32 C54 36 52 39 48 42 L50 49 L41 45 C39 46 38 46 36 46 C26 46 18 40 18 32 C18 24 26 18 36 18 Z" fill="#fff" stroke="#a00b12" stroke-width="3"/>
        <text x="13" y="24" font-family="Georgia, serif" font-weight="700" font-size="20" fill="#a00b12">“</text>
        <text x="29" y="44" font-family="Georgia, serif" font-weight="700" font-size="20" fill="#a00b12">”</text>
      </svg>
    </div>
    <h3 class="strategy__title">Communication</h3>
    <p class="strategy__quote">The Single biggest problem in communication is the illusion that is has taken place</p>
    <p class="strategy__source">Gordon B. Shale</p>
    <svg class="strategy__mark" style="left:194px" viewBox="0 0 22 16" aria-hidden="true"><g fill="#333"><circle cx="5" cy="11" r="4.5"/><path d="M1 10 C1 4 4 1 8 0 L8.6 1.6 C6 3 5 5 5 8 Z"/><circle cx="16" cy="11" r="4.5"/><path d="M12 10 C12 4 15 1 19 0 L19.6 1.6 C17 3 16 5 16 8 Z"/></g></svg>
  </article>

  <footer class="contact-bar">
    <svg width="30" height="20" viewBox="0 0 30 20" aria-hidden="true" fill="none" stroke="#fff" stroke-width="1.8">
      <rect x="1" y="1" width="28" height="18"/><path d="M1 1 L15 12 L29 1 M1 19 L11 9 M29 19 L19 9"/>
    </svg>
    <span class="contact-bar__email">info@themarlowegroup.com</span>
  </footer>

</main>
</body>
</html>
```